Occupational Therapist does home accessibility for disabled folks; needs business card design

We need a business card for a company in Portland, Oregon that specializes in making homes accessible, comfortable, and functional for people who are disabled or aging who would like to stay in THEIR home. Our medical background as Occupational Therapists allows us to translate the functional needs of the person into the recommendations for the design of the home remodel.

Target Market(s)

Elderly, children of elderly
People with disabilities, families of people with disabilities

Industry/Entity Type

Business

Contact Information for Business Card

Company name: HomeWise
Name: Danielle Reyes Crawford, OTR/L, CAPS, ECHM
Occupational Therapist, Home Modification & Accessibility Specialist
website: www.homewiseforyears.com
email: homewiseforyears@nestmail.example
phone: (503)218-4057
CCB #: 487315

Font styles to use
Sans Serif

Requirements
Must have
• My logo
• Easy to read font with contrasting background
• Please list the Services offered: Occupational Therapy, Home safety & accessibility assessments, Home modification consulting, project management
Nice to have
• Friendly, welcoming feel
Should not have
• Dark colored background

```html
<!DOCTYPE html>
<html lang="en">
<head>
<meta charset="utf-8">
<title>HomeWise Business Card</title>
<link rel="stylesheet" href="https://fonts.googleapis.com/css2?family=Lato:wght@300;400;700&display=swap">
<style>
  :root {
    --backdrop: #e2e2e2;
    --card: #ffffff;
    --brand-orange: #d17f2b;
    --brand-orange-shade: #a65a28;
    --brand-grey: #666666;
    --text-light: #ffffff;
  }
  html, body {
    margin: 0;
    padding: 0;
    width: 1200px;
    height: 1200px;
    overflow: hidden;
    background: var(--backdrop);
    font-family: "Lato", sans-serif;
  }
  .card {
    position: absolute;
    top: 480px;
    width: 437px;
    height: 242px;
    display: block;
  }
  .card--front { left: 106px; }
  .card--back { left: 641px; }
  .card-base { fill: var(--card); }
  .fill-orange { fill: var(--brand-orange); }
  .fill-shade { fill: var(--brand-orange-shade); }
  .fill-grey { fill: var(--brand-grey); }
  .fill-white { fill: var(--card); }
  .brand-name {
    font-family: "Lato", sans-serif;
    font-weight: 700;
  }
  .brand-name--front { font-size: 30px; fill: var(--brand-orange); }
  .brand-name--back { font-size: 44px; fill: var(--brand-orange); }
  .service-item {
    font-family: "Lato", sans-serif;
    font-weight: 300;
    font-size: 14.5px;
    fill: var(--brand-grey);
  }
  .holder-name {
    font-family: "Lato", sans-serif;
    font-weight: 400;
    font-size: 14px;
    fill: var(--text-light);
  }
  .holder-credentials {
    font-family: "Lato", sans-serif;
    font-weight: 300;
    font-size: 12.5px;
    fill: var(--text-light);
  }
  .contact-line {
    font-family: "Lato", sans-serif;
    font-weight: 300;
    font-size: 12.5px;
    letter-spacing: 0.3px;
    fill: var(--text-light);
  }
  .contact-line--long { font-size: 11px; letter-spacing: 0; }
  .contact-icon { fill: var(--text-light); }
</style>
</head>
<body>

<svg class="card card--front" viewBox="0 0 546 303" role="group" aria-label="Business card front">
  <rect class="card-base" x="0" y="0" width="546" height="303"/>
  <polygon class="fill-orange" points="334,0 546,0 546,303 252,303"/>
  <rect class="fill-orange" x="224" y="67" width="110" height="53"/>
  <polygon class="fill-shade" points="224,120 277,120 277,150"/>
  <polygon class="fill-white" points="316,0 334,0 252,303 234,303"/>
  <polygon class="fill-grey" points="313,0 332,0 248,303 229,303"/>
  <polygon class="fill-white" points="332,0 335,0 251,303 248,303"/>

  <g class="brand-lockup">
    <rect class="fill-grey" x="44" y="70" width="14" height="14"/>
    <text class="brand-name brand-name--front" x="66" y="88">HomeWise</text>
  </g>

  <g class="service-list">
    <rect class="fill-grey" x="30" y="164" width="7" height="7"/>
    <text class="service-item" x="48" y="172">HOME MODIFICATION</text>
    <rect class="fill-grey" x="30" y="184" width="7" height="7"/>
    <text class="service-item" x="48" y="192">OCCUPATIONAL THERAPIST</text>
    <rect class="fill-grey" x="30" y="203" width="7" height="7"/>
    <text class="service-item" x="48" y="211">ACCESSIBILITY SPECIALIST</text>
  </g>

  <g class="card-holder">
    <text class="holder-name" x="520" y="91" text-anchor="end" textLength="186" lengthAdjust="spacingAndGlyphs">DANIELLE REYES CRAWFORD</text>
    <text class="holder-credentials" x="520" y="110" text-anchor="end">OTR/L, CAPS, ECHM</text>
  </g>

  <g class="contact-list">
    <path class="contact-icon" d="M316,185 l3,-1 l1.5,3 l-1.5,1 q1,2.5 3,3.5 l1,-1.5 l3,1.5 l-1,3 q-6,0 -9,-9.5 z"/>
    <text class="contact-line" x="331" y="194">(503)218-4057</text>
    <rect class="contact-icon" x="315" y="211" width="9" height="6"/>
    <polyline points="315,211 319.5,215 324,211" fill="none" stroke="#d17f2b" stroke-width="1"/>
    <text class="contact-line contact-line--long" x="332" y="219" textLength="184" lengthAdjust="spacingAndGlyphs">homewiseforyears@nestmail.example</text>
    <circle cx="319.5" cy="237" r="4.5" class="contact-icon"/>
    <path d="M315,237 h9 M319.5,232.5 v9" stroke="#d17f2b" stroke-width="0.9"/>
    <text class="contact-line" x="332" y="241">www.homewiseforyears.com</text>
  </g>
</svg>

<svg class="card card--back" viewBox="0 0 546 303" role="group" aria-label="Business card back">
  <rect class="card-base" x="0" y="0" width="546" height="303"/>
  <polygon class="fill-orange" points="0,0 343,0 338,10 0,10"/>
  <polygon class="fill-grey" points="360,0 546,0 546,10 355,10"/>
  <polygon class="fill-orange" points="0,291 252,291 246,303 0,303"/>
  <polygon class="fill-grey" points="270,291 546,291 546,303 264,303"/>

  <g class="brand-lockup">
    <rect class="fill-grey" x="170" y="135" width="18" height="18"/>
    <text class="brand-name brand-name--back" x="198" y="160">HomeWise</text>
  </g>
</svg>

</body>
</html>
```